Need a book cover design for a Lumora Book

Book has a long title and sub title so lots of words to fit on the cover.

I can be flexible a bit with the sub title due to the length of it but ideally i can get a design that takes everything.

Here is the title:

Tidal Geology: The Roots of Erosion, Sedimentation, and Canyon Forming

Sub Title/Heading
An Easy Primer on Coastal Cliffs, Dune Drift, River Beds, and Delta Mapping Methods

```html
<!DOCTYPE html>
<html lang="en">
<head>
<meta charset="utf-8">
<title>Tidal Geology — Book Cover</title>
<link rel="stylesheet" href="https://fonts.googleapis.com/css2?family=Poppins:wght@400;600;700;800&display=swap">
<style>
  :root {
    --stage: #a3adad;
    --cover: #1f1f1f;
    --white: #ffffff;
    --purple-light: #c468f2;
    --purple-deep: #8b3fc6;
    --purple-author: #a64fe0;
    --green-light: #a2ea8a;
    --green-deep: #04a57f;
    --green-tag: #8fe07c;
  }
  * { margin: 0; padding: 0; box-sizing: border-box; }
  html, body {
    width: 1200px;
    height: 2400px;
    overflow: hidden;
    background: var(--stage);
    font-family: "Poppins", sans-serif;
  }
  .cover {
    position: absolute;
    left: 150px;
    top: 480px;
    width: 900px;
    height: 1440px;
    background: var(--cover);
    overflow: hidden;
    box-shadow: 0 10px 30px rgba(0,0,0,0.25);
  }
  .title {
    position: absolute;
    left: 66px;
    top: 70px;
    font-weight: 800;
    line-height: 0.9;
    letter-spacing: -2px;
  }
  .title-line {
    display: block;
    font-size: 156px;
    -webkit-background-clip: text;
    background-clip: text;
    color: transparent;
  }
  .title-top {
    background-image: linear-gradient(180deg, var(--purple-deep) 0%, var(--purple-light) 100%);
  }
  .title-bottom {
    background-image: linear-gradient(180deg, var(--green-light) 0%, var(--green-deep) 100%);
  }
  .subtitle {
    position: absolute;
    left: 69px;
    top: 405px;
    color: var(--white);
    font-size: 38px;
    line-height: 1.27;
  }
  .subtitle-strong { font-weight: 700; display: block; }
  .subtitle-light { font-weight: 400; display: block; }
  .art-main {
    position: absolute;
    left: 385px;
    top: 570px;
    width: 515px;
    height: 620px;
  }
  .art-side {
    position: absolute;
    left: 0;
    top: 595px;
    width: 130px;
    height: 280px;
  }
  .tagline {
    position: absolute;
    left: 69px;
    top: 990px;
    color: var(--white);
    font-size: 31px;
    line-height: 1.29;
    font-weight: 400;
  }
  .tagline-lead { color: var(--green-tag); font-weight: 700; display: block; }
  .tagline-rest { display: block; }
  .author {
    position: absolute;
    left: 64px;
    top: 1258px;
    color: var(--purple-author);
    font-size: 60px;
    font-weight: 700;
    letter-spacing: 11px;
    line-height: 1;
  }
</style>
</head>
<body>
  <main class="cover">
    <h1 class="title">
      <span class="title-line title-top">TIDAL</span>
      <span class="title-line title-bottom">GEOLOGY</span>
    </h1>

    <h2 class="subtitle">
      <span class="subtitle-strong">THE ROOTS</span>
      <span class="subtitle-strong">OF EROSION,</span>
      <span class="subtitle-light">SEDIMENTATION, AND</span>
      <span class="subtitle-light">CANYON FORMING</span>
    </h2>

    <svg class="art-side" role="img" aria-label="Small orbiting molecule illustration in purple and green" viewBox="0 0 130 280">
      <defs>
        <radialGradient id="side-glow" cx="30%" cy="45%" r="70%">
          <stop offset="0%" stop-color="#a2ea8a" stop-opacity="0.55"/>
          <stop offset="45%" stop-color="#8b3fc6" stop-opacity="0.35"/>
          <stop offset="100%" stop-color="#1f1f1f" stop-opacity="0"/>
        </radialGradient>
      </defs>
      <rect width="130" height="280" fill="url(#side-glow)"/>
    </svg>

    <svg class="art-main" role="img" aria-label="Large molecule with purple orbit rings illustration" viewBox="0 0 515 620">
      <defs>
        <radialGradient id="main-glow" cx="55%" cy="50%" r="55%">
          <stop offset="0%" stop-color="#c8f29a" stop-opacity="0.75"/>
          <stop offset="35%" stop-color="#5cbf8c" stop-opacity="0.5"/>
          <stop offset="65%" stop-color="#8b3fc6" stop-opacity="0.4"/>
          <stop offset="100%" stop-color="#1f1f1f" stop-opacity="0"/>
        </radialGradient>
      </defs>
      <rect width="515" height="620" fill="url(#main-glow)"/>
    </svg>

    <p class="tagline">
      <span class="tagline-lead">An Easy Primer</span>
      <span class="tagline-lead">on Coastal Cliffs,</span>
      <span class="tagline-rest">Dune Drift, River</span>
      <span class="tagline-rest">Beds, and Delta</span>
      <span class="tagline-rest">Mapping Methods</span>
    </p>

    <p class="author">MARA QUILLON</p>
  </main>
</body>
</html>
```